Small company security and risk consulting startup needs an explosive message via marketing colla...

Need a two page (front/back) flyer that calls out our three primary service areas incorporating brandmill developed logo and website visuals. Something that grabs attention at first glance to entice the viewer to read and connect for a services consultation. I will need the ability to make minor adjustments and add language.

```html
<!DOCTYPE html>
<html lang="en">
<head>
<meta charset="utf-8">
<title>Sentinel Ridge Consulting Services – Flyer</title>
<link rel="stylesheet" href="https://fonts.googleapis.com/css2?family=Open+Sans:wght@400;600;700&display=swap">
<style>
  :root{
    --stage:#ececec;
    --paper:#ffffff;
    --ink:#1b1b1b;
    --ink-soft:#3a3a3a;
    --charcoal:#161616;
    --charcoal-2:#2c2c2c;
    --red:#d71f26;
    --red-deep:#8e1017;
    --blue:#2a3f97;
    --silver:#c9c9c9;
    --band:#ededed;
  }
  *{box-sizing:border-box;margin:0;padding:0}
  html,body{width:1200px;height:769px;overflow:hidden;background:var(--stage)}
  body{font-family:"Open Sans",Arial,sans-serif;color:var(--ink);position:relative}
  .page{position:absolute;top:41px;width:526px;height:681px;background:var(--paper);overflow:hidden;box-shadow:0 4px 14px rgba(0,0,0,.25)}
  .page--front{left:45px}
  .page--back{left:606px}
  .shapes{position:absolute;inset:0;width:526px;height:681px}
  .brand{position:absolute;text-align:center;color:var(--silver)}
  .brand__name{font-weight:700;font-size:27px;letter-spacing:.5px;color:#d9d9d9;display:flex;align-items:center;justify-content:center;gap:8px}
  .brand__mark{width:14px;height:14px;background:var(--red);display:inline-block}
  .brand__line{font-size:10.5px;font-weight:600;letter-spacing:4.5px;color:#fff;margin-top:4px}
  .brand__motto{font-size:7px;letter-spacing:2.4px;color:var(--red);margin-top:3px}
  .section-title{position:absolute;left:0;right:0;top:320px;text-align:center;font-size:18px;font-weight:600;color:var(--ink)}
  .section-rule{position:absolute;top:339px;left:203px;width:120px;height:1px;background:var(--ink)}
  .copy{position:absolute;left:90px;right:90px;text-align:center;font-size:8.4px;line-height:11.5px;color:var(--ink-soft)}
  .service{position:absolute;top:440px;width:120px;text-align:center;color:#fff}
  .service__icon{display:block;margin:0 auto 6px;width:26px;height:26px}
  .service__name{font-size:9.5px;font-weight:700;line-height:11px}
  .service__text{font-size:5.8px;line-height:8px;opacity:.75;margin-top:5px}
  .contact{position:absolute;left:18px;top:618px;list-style:none;color:#fff;font-size:8.6px;line-height:13.7px}
  .contact li{display:flex;align-items:center;gap:7px}
  .contact svg{width:10px;height:10px;flex:none}
  .social{position:absolute;top:657px;display:flex;gap:9px}
  .social span{width:17px;height:17px;border:1px solid #fff;border-radius:50%;display:block}
  .review{position:absolute;left:22px;right:22px;top:466px;color:#fff;text-align:center}
  .review__title{font-size:14.5px;font-weight:400;margin-bottom:10px}
  .review__body{font-size:8.2px;line-height:11.3px;text-align:justify}
</style>
</head>
<body>

<!-- Front page -->
<section class="page page--front">
  <svg class="shapes" viewBox="0 0 526 681" aria-hidden="false">
    <defs>
      <radialGradient id="hexGlow" cx="50%" cy="40%" r="70%">
        <stop offset="0" stop-color="#2a2a2a"/>
        <stop offset=".7" stop-color="#171717"/>
        <stop offset="1" stop-color="#3a0a0c"/>
      </radialGradient>
      <linearGradient id="footDark" x1="0" y1="0" x2="1" y2="1">
        <stop offset="0" stop-color="#3a3a3a"/>
        <stop offset="1" stop-color="#0d0d0d"/>
      </linearGradient>
    </defs>
    <polygon points="0,250 263,296 526,250 526,258 263,304 0,258" fill="var(--red)"/>
    <polygon role="img" aria-label="Dark honeycomb pattern with red glowing edges" points="0,0 526,0 526,250 263,296 0,250" fill="url(#hexGlow)"/>
    <rect x="0" y="434" width="526" height="135" fill="var(--band)"/>
    <polygon points="88,434 161,434 222,569 27,569" fill="#262626"/>
    <polygon points="165,434 351,434 280,569 245,569" fill="var(--red)"/>
    <polygon points="355,434 455,434 482,569 285,569" fill="var(--blue)"/>
    <polygon points="0,594 526,652 526,681 0,681" fill="url(#footDark)"/>
    <polygon points="305,628 526,611 526,650" fill="var(--red)"/>
    <circle cx="487" cy="611" r="27" fill="#fff" stroke="var(--blue)" stroke-width="3"/>
    <circle cx="487" cy="611" r="18" fill="none" stroke="var(--red)" stroke-width="2"/>
  </svg>

  <div class="brand" style="left:0;right:0;top:128px">
    <div class="brand__name"><span class="brand__mark"></span>Sentinel Ridge</div>
    <div class="brand__line">CONSULTING SERVICES</div>
    <div class="brand__motto">commitment · integrity · results</div>
  </div>

  <h2 class="section-title">ABOUT US</h2>
  <div class="section-rule"></div>
  <p class="copy" style="top:357px">Nunc tempus felis vitae urna Vivamus porttitor neque at volutpat rutrum purus nisi eleifend libero a tempus libero lectus feugiat felis Morbi diam</p>
  <p class="copy" style="top:392px">mauris viverra in gravida eu mattis in ante Morbi eget arcu Morbi porta libero id ullamcorper nonummy nibh ligula pulvinar metus eget consectetuer augue nisi quis lacus Ut ac mi quis lacus mollis aliquam Curabitur iaculis</p>

  <div class="service" style="left:65px">
    <svg class="service__icon" viewBox="0 0 26 26" fill="none" stroke="#fff" stroke-width="1.4"><rect x="3" y="4" width="20" height="14" rx="1"/><path d="M9 22h8M13 18v4"/><circle cx="13" cy="11" r="2.5"/></svg>
    <div class="service__name">NATIONAL<br>SECURITY</div>
    <div class="service__text">Morbi diam mauris viverra in gravida eu mattis in an</div>
  </div>
  <div class="service" style="left:198px">
    <svg class="service__icon" viewBox="0 0 26 26" fill="none" stroke="#fff" stroke-width="1.4"><circle cx="13" cy="13" r="5"/><path d="M13 3v4M13 19v4M3 13h4M19 13h4M6 6l3 3M17 17l3 3M20 6l-3 3M6 20l3-3"/></svg>
    <div class="service__name">RISK MANAGEMENT<br>SERVICES</div>
    <div class="service__text">Morbi diam mauris viverra in gravida eu mattis in an</div>
  </div>
  <div class="service" style="left:322px">
    <svg class="service__icon" viewBox="0 0 26 26" fill="none" stroke="#fff" stroke-width="1.4"><rect x="3" y="3" width="13" height="9" rx="1"/><rect x="10" y="12" width="13" height="9" rx="1"/><path d="M6 12v3l3-3"/></svg>
    <div class="service__name">CONSULTING<br>SERVICES</div>
    <div class="service__text">Morbi diam mauris viverra in gravida eu mattis in an</div>
  </div>

  <ul class="contact">
    <li><svg viewBox="0 0 10 10"><rect width="10" height="10" rx="2" fill="var(--red)"/><path d="M3 2.5l1 2-1 1c.5 1 1 1.5 2 2l1-1 2 1-.5 1.5C5 9 1 5 2 2.5z" fill="#fff"/></svg>(555) 014 2290</li>
    <li><svg viewBox="0 0 10 10"><rect width="10" height="10" rx="2" fill="var(--red)"/><path d="M2 3h6v4H2zM2 3l3 2.2L8 3" fill="none" stroke="#fff" stroke-width=".8"/></svg>hello@sentinelridge.example</li>
    <li><svg viewBox="0 0 10 10"><rect width="10" height="10" rx="2" fill="var(--red)"/><circle cx="5" cy="5" r="2.8" fill="none" stroke="#fff" stroke-width=".8"/></svg>www.sentinelridge.example</li>
    <li><svg viewBox="0 0 10 10"><rect width="10" height="10" rx="2" fill="var(--red)"/><path d="M5 8.5L2.8 5a2.3 2.3 0 1 1 4.4 0z" fill="#fff"/></svg>42 Harbor Lane, Suite 7, Austin TX 78701</li>
  </ul>
  <div class="social" style="left:394px"><span></span><span></span><span></span><span></span></div>
</section>

<!-- Back page -->
<section class="page page--back">
  <svg class="shapes" viewBox="0 0 526 681">
    <defs>
      <radialGradient id="panelDark" cx="45%" cy="45%" r="65%">
        <stop offset="0" stop-color="#4a4a4a"/>
        <stop offset="1" stop-color="#101010"/>
      </radialGradient>
      <linearGradient id="photoTone" x1="0" y1="0" x2="1" y2="1">
        <stop offset="0" stop-color="#9a9a9a"/>
        <stop offset=".5" stop-color="#4e4e4e"/>
        <stop offset="1" stop-color="#1e1e1e"/>
      </linearGradient>
      <linearGradient id="reviewRed" x1="0" y1="0" x2="1" y2="1">
        <stop offset="0" stop-color="var(--red)"/>
        <stop offset="1" stop-color="var(--red-deep)"/>
      </linearGradient>
      <linearGradient id="footDark2" x1="0" y1="0" x2="1" y2="1">
        <stop offset="0" stop-color="#3a3a3a"/>
        <stop offset="1" stop-color="#0d0d0d"/>
      </linearGradient>
    </defs>
    <polygon role="img" aria-label="Black and white photo of a consultant presenting in a meeting room" points="247,0 526,0 526,296 247,296 287,148" fill="url(#photoTone)"/>
    <polygon points="0,0 247,0 287,148 247,296 0,296" fill="url(#panelDark)"/>
    <polyline points="247,0 287,148 247,296" fill="none" stroke="var(--red)" stroke-width="4"/>
    <polygon points="11,438 512,430 512,584 263,592 11,584" fill="url(#reviewRed)"/>
    <polygon points="0,594 526,652 526,681 0,681" fill="url(#footDark2)"/>
    <polygon points="305,628 526,611 526,650" fill="var(--red)"/>
    <circle cx="487" cy="611" r="27" fill="#fff" stroke="var(--blue)" stroke-width="3"/>
    <circle cx="487" cy="611" r="18" fill="none" stroke="var(--red)" stroke-width="2"/>
  </svg>

  <div class="brand" style="left:10px;width:260px;top:168px">
    <div class="brand__name" style="font-size:24px"><span class="brand__mark"></span>Sentinel Ridge</div>
    <div class="brand__line" style="font-size:9.5px;letter-spacing:4px">CONSULTING SERVICES</div>
    <div class="brand__motto">commitment · integrity · results</div>
  </div>

  <h2 class="section-title">WHY WE ARE</h2>
  <div class="section-rule"></div>
  <p class="copy" style="top:357px">Nunc tempus felis vitae urna Vivamus porttitor neque at volutpat rutrum purus nisi eleifend libero a tempus libero lectus feugiat felis Morbi diam</p>
  <p class="copy" style="top:392px">mauris viverra in gravida eu mattis in ante Morbi eget arcu Morbi porta libero id ullamcorper nonummy nibh ligula pulvinar metus eget consectetuer augue nisi quis lacus Ut ac mi quis lacus mollis aliquam Curabitur iaculis</p>

  <div class="review">
    <h3 class="review__title">The decision-making process of Strategic Defence and Security Review</h3>
    <p class="review__body">Nunc tempus felis vitae urna Vivamus porttitor neque at volutpat rutrum purus nisieleifend libero a tempus libero lectus feugiat felis Morbi diam mauris viverra in gravida eu mattis in ante Morbi eget arcu Morbi porta libero id ullamcorper nonummy nibh ligula pulvinar metus eget consectetuer augue nisi quis lacus Ut ac mi quis lacus mollis aliquam Curabitur iaculis Nunc tempus felis vitae urna Vivamus porttitor neque at volutpat rutrum purus nisieleifend libero a tempus libero lectus feugiat felis Morbi diam mauris viverra in gravida eu mattis in ante Morbi eget arcu Morbi porta libero id ullamcorper nonummy nibh ligula pulvinar metus eget consectetuer augue nisi quis lacus Ut ac mi quis lacus mollis aliquam Curabitur</p>
  </div>

  <ul class="contact">
    <li><svg viewBox="0 0 10 10"><rect width="10" height="10" rx="2" fill="var(--red)"/><path d="M3 2.5l1 2-1 1c.5 1 1 1.5 2 2l1-1 2 1-.5 1.5C5 9 1 5 2 2.5z" fill="#fff"/></svg>(555) 014 2290</li>
    <li><svg viewBox="0 0 10 10"><rect width="10" height="10" rx="2" fill="var(--red)"/><path d="M2 3h6v4H2zM2 3l3 2.2L8 3" fill="none" stroke="#fff" stroke-width=".8"/></svg>hello@sentinelridge.example</li>
    <li><svg viewBox="0 0 10 10"><rect width="10" height="10" rx="2" fill="var(--red)"/><circle cx="5" cy="5" r="2.8" fill="none" stroke="#fff" stroke-width=".8"/></svg>www.sentinelridge.example</li>
    <li><svg viewBox="0 0 10 10"><rect width="10" height="10" rx="2" fill="var(--red)"/><path d="M5 8.5L2.8 5a2.3 2.3 0 1 1 4.4 0z" fill="#fff"/></svg>42 Harbor Lane, Suite 7, Austin TX 78701</li>
  </ul>
  <div class="social" style="left:394px"><span></span><span></span><span></span><span></span></div>
</section>

</body>
</html>
```